Law Office needs stationery design and business card

I currently have been using the same letterhead for the last 8 years. Since i 'm about to adding another location, I want to revamp my letterhead and business card. I already have a logo i'm happy with. I will upload my current letterhead, fax sheet, envelope, and logos. I need a business card also. I have 2 locations, 1 phone number, 1 fax line, website, etc. If possible and fitting with the design, I would like to keep the same information listed currently on the letterhead.

**Keep in mind, I also NEED A FAX SHEET COVER. thank you

Hello, Please submit a Gray Scale or Black and White version of your designs also, since most of the time I will be printing NON color stationery. I will seldom use a color print for my letterhead, I would like to have a color version for my benefit, however i will print in grayscale majority of the time . For the Business Card, that can just be in color. When I get my business cards they will be in color.Thank youEnrique Added Sunday, September 18, 2016

```html
<!DOCTYPE html>
<html lang="en">
<head>
<meta charset="utf-8">
<title>Marlowe Law – Stationery</title>
<link href="https://fonts.googleapis.com/css2?family=Montserrat:wght@400;600;700&display=swap" rel="stylesheet">
<style>
  :root{
    --bg:#e6e6e6;
    --paper:#f2f2f2;
    --ink:#231f1c;
    --gold:#b99b63;
    --line:#8a8a8a;
    --muted:#5a5a5a;
  }
  *{box-sizing:border-box;margin:0;padding:0}
  html,body{width:1200px;height:816px;overflow:hidden;background:var(--bg)}
  body{position:relative;font-family:"Montserrat",Arial,sans-serif;color:var(--ink)}
  .sheet{position:absolute;width:300px;height:388px;background:var(--paper);box-shadow:0 3px 8px rgba(0,0,0,.12);overflow:hidden}
  .sheet--fax{left:110px;top:214px}
  .sheet--letter{left:450px;top:214px}
  .accent{position:absolute;left:0;top:0;width:90px;height:64px;background:linear-gradient(135deg,var(--ink) 0%,var(--ink) 45%,var(--gold) 100%)}
  .card .accent{width:52px;height:38px}
  .brand{position:absolute;left:0;right:0;top:26px;text-align:center}
  .brand__mark{display:block;width:14px;height:14px;margin:0 auto 5px;background:var(--ink)}
  .brand__name{font-weight:600;font-size:10px;letter-spacing:1.5px;color:var(--ink)}
  .doc-title{position:absolute;left:0;right:0;top:66px;text-align:center;font-weight:700;font-size:10px;letter-spacing:.5px}
  .fax-table{position:absolute;left:40px;top:94px;width:220px;border-collapse:collapse;table-layout:fixed;font-size:6px;font-weight:700}
  .fax-table td{border:1px solid var(--line);height:13px;padding:0 3px;vertical-align:middle}
  .fax-table .label{width:30px}
  .fax-table .re{height:22px;vertical-align:top;padding-top:2px}
  .fax-rule{position:absolute;left:40px;right:40px;border-top:1px dashed var(--line)}
  .footer{position:absolute;left:0;right:0;bottom:18px;text-align:center;font-size:4.6px;line-height:7px;color:var(--muted)}
  .footer__web{font-weight:700;color:var(--ink)}
  .card{position:absolute;width:210px;height:120px;background:var(--paper);box-shadow:0 3px 8px rgba(0,0,0,.12);overflow:hidden}
  .card--front{left:820px;top:214px}
  .card--back{left:820px;top:360px}
  .card--front .brand{top:38px}
  .card--front .brand__name{font-size:11px}
  .card--back .brand{left:auto;right:16px;top:12px;text-align:right}
  .card--back .brand__mark{width:9px;height:9px;margin:0 0 3px auto}
  .card--back .brand__name{font-size:7px}
  .card__rule{position:absolute;left:16px;right:16px;top:52px;border-top:1px solid var(--gold)}
  .card__person{position:absolute;left:16px;top:60px;font-size:8px;font-weight:700;letter-spacing:.5px}
  .card__role{position:absolute;left:16px;top:71px;font-size:5.5px;color:var(--gold);font-weight:600}
  .card__contact{position:absolute;left:16px;top:84px;font-size:5px;line-height:7.5px;color:var(--muted)}
</style>
</head>
<body>

<section class="sheet sheet--fax" aria-label="Fax cover sheet">
  <div class="accent" role="img" aria-label="Black and gold corner accent"></div>
  <div class="brand"><span class="brand__mark"></span><span class="brand__name">MARLOWE LAW</span></div>
  <h1 class="doc-title">FAX COVER</h1>
  <table class="fax-table">
    <tr><td class="label">To</td><td></td><td class="label">From</td><td></td></tr>
    <tr><td class="label">Fax #</td><td></td><td class="label">Fax #</td><td></td></tr>
    <tr><td class="label re">Re:</td><td class="re" colspan="3"></td></tr>
  </table>
  <div class="fax-rule" style="top:200px"></div>
  <div class="fax-rule" style="top:270px"></div>
  <footer class="footer">
    100 Harbor Street, Suite 200, Easton, PA 18040 | 45 Mill Road, Newtown, PA 18940<br>
    Tel 555-010-2400 | Fax 555-010-2401 | office@marlowelaw.com<br>
    <span class="footer__web">www.marlowelaw.com</span>
  </footer>
</section>

<section class="sheet sheet--letter" aria-label="Letterhead">
  <div class="accent" role="img" aria-label="Black and gold corner accent"></div>
  <div class="brand"><span class="brand__mark"></span><span class="brand__name">MARLOWE LAW</span></div>
  <h1 class="doc-title">LAW OFFICE</h1>
  <footer class="footer">
    100 Harbor Street, Suite 200, Easton, PA 18040 | 45 Mill Road, Newtown, PA 18940<br>
    Tel 555-010-2400 | Fax 555-010-2401 | office@marlowelaw.com<br>
    <span class="footer__web">www.marlowelaw.com</span>
  </footer>
</section>

<section class="card card--front" aria-label="Business card front">
  <div class="brand"><span class="brand__mark"></span><span class="brand__name">MARLOWE LAW</span></div>
</section>

<section class="card card--back" aria-label="Business card back">
  <div class="accent" role="img" aria-label="Black and gold corner accent"></div>
  <div class="brand"><span class="brand__mark"></span><span class="brand__name">MARLOWE LAW</span></div>
  <div class="card__rule"></div>
  <p class="card__person">GUSTAVO MARLOWE</p>
  <p class="card__role">Attorney at Law</p>
  <p class="card__contact">
    Tel 555-010-2400 · Fax 555-010-2401<br>
    office@marlowelaw.com<br>
    100 Harbor Street, Easton, PA 18040
  </p>
</section>

</body>
</html>
```